International Patent Law Firm Needs a New Website Design

We are an international, German-based patent law firm and are in need for a new website design.

Our current (old-fashioned) website is

www.lwpt.example

Our Corporate Identity features that we want to keep are as follows.

1. Our LWPT logo in blue color on white background.

2. The tent roof design of the Harbour Crest Arena.

We attach our current LWPT presentation, which gives you an idea of who we are, what our business is and what distinguishes us.

The new website design should express that we provide very reliable, high-quality Intellectual Property services, including patent and trademark services worldwide.

On the one hand, it should professional, on the other it should look young.

The managing partners of our patent law firm are in their 30ies and their 40ies, which is comparably young for a patent law firm of our size. Our team comprises about 20 patent attorneys and altogether 45 people.

Websites of competitors that we like are as follows.

http://www.rml.example
http://dorsellquaint.example
http://www.pellard.example
http://www.vrmlaw.example (here we like the structure, rather than the design)

There are two features that all these websites have in common and that we also would like to have implemented in our new website design.

1. A clear and self-explaining main menu in the header.

For example:

HOME OUR FIRM WHAT WE DO WHO WE ARE OUR CLIENTS OUR FEES CONTACT US

2. At least on the main page: A background picture filling the entire screen and having an appealing graphic. Maybe the tent roof of the Harbour Crest Arena?

Further points that we believe to be important are as follows:

1. Our new website should have a simple menu navigation (not as complicated as the current one). It should have two levels, namely the main page and the subpages, that are all directly accessible via the main page, so that all the content can be reached with two clicks.

2. On the WHO WE ARE subpage we like the solution that there is a list of the names of the patent attorneys in the left column, and upon clicking on a name the full profile of the patent attorney including a photograph of the partner will appear. We will have new photographs of our team prepared and supplied to you.

3. On the WHAT WE DO subpage we like the solution that there is a list of the headlines of our fields of activity, like PATENTS, and upon clicking on a headline a more detailed description of the respective field of activity will appear.

4. Our new website should contain less content than our current website. The text will be supplied by us.

5. What is also very important is that the design will be optimized for access by PCs, by tablets and by smart phones (responsive design).

6. We will need both English and German language versions of the website, including all the subpages. We will provide you with the updated text for all the pages.

Thanks very much in advance for your work and your suggestion.

Best regards,

Jonas Retterby (Partner)

Target Market(s)

Innovative and Patenting Firms worldwide, Innovators, Inventors, Potential new Employees

Industry/Entity Type

Lawyer

Number of Pages Required

5+ page

Font styles to use
Sans Serif

Colors
0555a3
0293ce

Requirements
Must have
• New appealing and modern website, self-explaining and easy menu structure
Nice to have
• Maybe some appealing design showing that we are constantly at the edge of the new technical development
Should not have
• May not look old-fashioned, no complicated menu

```html
<!DOCTYPE html>
<html lang="en">
<head>
<meta charset="utf-8">
<title>LWPT Law Firm</title>
<link href="https://fonts.googleapis.com/css2?family=Open+Sans:ital,wght@0,400;0,600;0,700;1,400;1,700&display=swap" rel="stylesheet">
<style>
:root{
  --brand:#0555a3;
  --accent:#0293ce;
  --nav-link:#3aa6e6;
  --dark:#1d1d1d;
  --field:#121212;
  --white:#ffffff;
  --text:#333333;
  --footer-text:#7fb6e6;
}
*{margin:0;padding:0;box-sizing:border-box}
html,body{width:1093px;height:1200px;overflow:hidden}
body{font-family:"Open Sans",sans-serif;background:var(--white);color:var(--text);position:relative}
.site-header{position:absolute;left:0;top:0;width:1093px;height:80px;background:var(--brand)}
.brand-name{position:absolute;left:90px;top:18px;color:var(--white);font-size:30px;font-weight:400;letter-spacing:4px}
.brand-sub{position:absolute;left:91px;top:60px;color:var(--white);font-size:6.5px;font-weight:700;letter-spacing:.2px}
.search{position:absolute;left:742px;top:18px;width:130px;height:16px;border:1px solid #0a3f7a;background:var(--brand);display:flex;align-items:center}
.search span{font-size:7px;font-style:italic;color:var(--white);padding-left:4px;flex:1}
.search svg{margin-right:4px}
.social{position:absolute;top:18px;width:16px;height:16px}
.social.s1{left:885px;background:var(--white)}
.social.s2{left:904px;background:#0a4b93}
.social.s3{left:921px;background:#0a4b93}
.flag{position:absolute;top:18px;width:24px;height:15px}
.flag.en{left:948px}
.flag.de{left:977px}
.main-nav{position:absolute;top:49px;right:92px;display:flex;font-size:11.5px;font-weight:700;text-transform:uppercase}
.main-nav a{color:var(--nav-link);text-decoration:none;position:relative;padding:0 17px}
.main-nav a+a::before{content:"";position:absolute;left:0;top:2px;height:11px;border-left:1px solid #2f7bc4}
.main-nav a.active{color:var(--white)}
.main-nav a.active::after{content:"";position:absolute;left:17px;right:17px;top:28px;height:3px;background:var(--white)}
.main-nav a:last-child{padding-right:0}
.hero{position:absolute;left:0;top:80px;width:1093px;height:440px;background:radial-gradient(ellipse at 75% 30%,#6a4030 0%,#3a1d16 45%,#1c0e0b 100%)}
.hero-content{position:absolute;left:0;right:0;top:70px;text-align:center;color:var(--white)}
.hero-name{font-size:68px;font-weight:400;letter-spacing:10px;line-height:1}
.hero-partners{font-size:16px;font-weight:700;margin-top:22px}
.hero-rule{width:346px;height:1px;background:var(--white);margin:18px auto 14px}
.hero-tag{font-size:17px;font-weight:700;line-height:19px;text-shadow:0 1px 3px rgba(0,0,0,.6)}
.btn{display:inline-block;background:var(--accent);color:var(--white);font-weight:700;text-decoration:none;text-transform:uppercase;text-align:center}
.hero .btn{margin-top:14px;width:160px;height:48px;line-height:48px;font-size:14.5px}
.welcome{position:absolute;left:0;top:520px;width:1093px;height:238px;text-align:center}
.welcome h1{margin-top:37px;font-size:20px;font-weight:400;color:var(--brand)}
.welcome h1 strong{color:var(--accent);font-weight:700}
.welcome p{font-size:11.5px;line-height:13.6px;color:var(--text);width:900px;margin:14px auto 0}
.welcome p+p{margin-top:13px}
.welcome .btn{margin-top:19px;width:132px;height:35px;line-height:35px;font-size:11.5px}
.info{position:absolute;left:0;top:758px;width:1093px;height:400px;background:var(--dark);color:var(--white)}
.info h2{font-size:13.5px;font-weight:700;color:var(--accent);position:absolute}
.info h2::after{content:"";position:absolute;left:0;top:25px;width:33px;height:2px;background:var(--white)}
.map-col h2{left:92px;top:32px}
.map-note{position:absolute;left:92px;top:65px;font-size:9.5px;line-height:12px}
.map-note a{color:var(--accent);font-weight:700;font-style:italic}
.map{position:absolute;left:92px;top:97px;width:365px;height:271px;border:3px solid var(--brand);background:linear-gradient(160deg,#0aa0d8,#0288c2)}
.form h2{left:480px;top:32px}
.field{position:absolute;left:481px;width:520px;background:var(--field);font-size:9.5px;padding:11px 11px;color:var(--white)}
.f1{top:71px;height:32px}.f2{top:111px;height:32px}.f3{top:151px;height:32px}.f4{top:191px;height:48px}
.submit{position:absolute;left:481px;top:248px;width:520px;height:32px;line-height:32px;font-size:9.5px;background:var(--accent);text-align:center;font-weight:700}
.contact-info h2{left:480px;top:295px}
.ci{position:absolute;top:334px;font-size:9.5px;line-height:11.5px}
.ci b{display:block;color:var(--accent);font-weight:700}
.c1{left:481px}.c2{left:648px}.c3{left:769px}.c4{left:906px}
.site-footer{position:absolute;left:0;top:1158px;width:1093px;height:42px;background:var(--brand);text-align:center;line-height:42px;font-size:10px;color:var(--footer-text)}
.site-footer .sep{display:inline-block;height:12px;border-left:1px solid var(--footer-text);margin:0 7px;vertical-align:middle}
.site-footer strong{color:var(--white)}
</style>
</head>
<body>
<header class="site-header">
  <div class="brand-name">LWPT</div>
  <div class="brand-sub">LANFORD • WENDT-PAULSEN • THORELL</div>
  <div class="search"><span>Enter Keyword</span>
    <svg width="10" height="10" viewBox="0 0 10 10"><circle cx="4" cy="4" r="3" fill="none" stroke="#fff" stroke-width="1.5"/><line x1="6.2" y1="6.2" x2="9" y2="9" stroke="#fff" stroke-width="1.5"/></svg>
  </div>
  <div class="social s1"></div><div class="social s2"></div><div class="social s3"></div>
  <svg class="flag en" viewBox="0 0 24 15"><rect width="24" height="15" fill="#1f3a8a"/><path d="M0 0L24 15M24 0L0 15" stroke="#fff" stroke-width="3"/><path d="M0 0L24 15M24 0L0 15" stroke="#c8102e" stroke-width="1"/><path d="M12 0V15M0 7.5H24" stroke="#fff" stroke-width="5"/><path d="M12 0V15M0 7.5H24" stroke="#c8102e" stroke-width="3"/></svg>
  <svg class="flag de" viewBox="0 0 24 15"><rect width="24" height="5" fill="#000"/><rect y="5" width="24" height="5" fill="#dd0000"/><rect y="10" width="24" height="5" fill="#ffce00"/></svg>
  <nav class="main-nav">
    <a class="active" href="#">Home</a><a href="#">Our Firm</a><a href="#">What We Do</a><a href="#">Who We Are</a><a href="#">Our Clients</a><a href="#">Our Fees</a><a href="#">Contact Us</a>
  </nav>
</header>

<section class="hero" role="img" aria-label="Photograph of a wooden judge's gavel on law books with brass scales of justice against a warm brown background">
  <div class="hero-content">
    <div class="hero-name">LWPT</div>
    <div class="hero-partners">LANFORD • WENDT-PAULSEN • THORELL</div>
    <div class="hero-rule"></div>
    <div class="hero-tag">European and German Patent Attorneys<br>European Trademark and Design Attorneys<br>Established 1985 - in Munich</div>
    <a class="btn" href="#">Know More</a>
  </div>
</section>

<section class="welcome">
  <h1>Welcome to <strong>lwpt</strong> Law Firm</h1>
  <p>The name "LWPT" derives from the full name of "Lanford, Wendt-Paulsen, Thorell" Patent Law Firm. LWPT is a medium-sized patent law firm by German standards, located in Munich, the seat of both the German Patent and Trademark Office and the European Patent Office. LWPT was founded in year 1985 by Dr. Erik Lanford, Dr. Mara Wendt-Paulsen and Paul Thorell.</p>
  <p>LWPT is constantly recruiting and training further qualified personnel to keep up with its growing business.</p>
  <a class="btn" href="#">Learn More</a>
</section>

<section class="info">
  <div class="map-col">
    <h2>lwpt Map</h2>
    <p class="map-note">Find your way with us. Necessary information for your journey to us,<br><a href="#">Download PDF</a></p>
    <div class="map" role="img" aria-label="Road map of Munich showing motorways, the city ring and the firm's location near the main station"></div>
  </div>
  <div class="form">
    <h2>Contact Us</h2>
    <div class="field f1">Name</div>
    <div class="field f2">Email</div>
    <div class="field f3">Subject</div>
    <div class="field f4">Message</div>
    <div class="submit">SUBMIT</div>
  </div>
  <div class="contact-info">
    <h2>Contact Information</h2>
    <div class="ci c1"><b>Address</b>Lindenweg 14<br>D-80331 München Germany</div>
    <div class="ci c2"><b>Email</b>mail@lwpt.example</div>
    <div class="ci c3"><b>Telephone</b>+49 / 89 / 00 11 22 0</div>
    <div class="ci c4"><b>Fax</b>+49 / 89 / 00 11 22 99</div>
  </div>
</section>

<footer class="site-footer">Liability Clause<span class="sep"></span>Copyright 2016. <strong>LWPT Law Firm</strong>. All Rights Reserved.</footer>
</body>
</html>
```